Web Design Project

We are building a site on Wordpress that will sell signed posters from various popular music artists - the name of the site is The Harlow Lane Studio. Consumers will be able to select from a list of personal messages and once they purchase, receive a high quality unique poster from the artist with a rendered handwriting based on the artist agreement.
We don't want anything too complicated, but would prefer a modern clean aesthetic. This is an e-commerce site, and will include a basic shopping cart. The artist galleries will be straightforward and may include some branding in the artist's look and feel.
Some sites to consider: kelvo.com, brimwexhall.com, quorble.com - but we would like it a bit cleaner and less busy.
Reason: I will be accepting designs up until Sunday evening EST. Thank you!
Reason: Thank you for your submissions! The client is reviewing the submissions and needs to run this by management before we select.
Reason: We are still delayed on the client's end as they are doing some logo and color re-designs.
Thanks for your patience.
Reason: We are trying to confirm a design choice with the client. Apologies for the delay!

```html
<!DOCTYPE html>
<html lang="en">
<head>
<meta charset="utf-8">
<title>The Harlow Lane Studio</title>
<link href="https://fonts.googleapis.com/css2?family=Cinzel:wght@400;500&family=Open+Sans:wght@400;600&family=Kalam:wght@400&display=swap" rel="stylesheet">
<style>
:root{
  --white:#ffffff;
  --orange:#fdb525;
  --orange-side:#fbac17;
  --orange-band:#f4a212;
  --orange-quote:#f8ab1c;
  --ink:#1f1a14;
  --link-blue:#3a6fd8;
  --pink:#e0245e;
  --teal-a:#9fe0da;
  --teal-b:#5ec3bc;
  --brown-a:#4a2a0c;
  --brown-b:#5a3210;
  --ribbon:#dfe5ee;
  --ribbon-edge:#b8c2d0;
}
*{margin:0;padding:0;box-sizing:border-box}
html,body{width:1200px;height:877px;overflow:hidden}
body{position:relative;background:var(--orange);font-family:"Open Sans",sans-serif;color:var(--white)}
.abs{position:absolute}
.pattern-side{left:1058px;top:0;width:142px;height:877px;background:linear-gradient(135deg,var(--brown-a),var(--brown-b))}
.pattern-bottom{left:0;top:820px;width:1200px;height:57px;background:linear-gradient(90deg,var(--brown-b),var(--brown-a))}
.header{left:0;top:0;width:1033px;height:97px;background:var(--white)}
.main{left:208px;top:97px;width:850px;height:723px;background:var(--orange)}
.sidebar{left:0;top:97px;width:208px;height:703px;background:var(--orange-side)}
.studio-name{left:24px;top:70px;font-size:13px;font-weight:600;color:var(--ink);white-space:nowrap}
.account-links{top:30px;font-size:11.5px;color:var(--link-blue);font-weight:600}
.nav{top:71px;font-family:"Cinzel",serif;font-size:13px;color:var(--ink);letter-spacing:.3px}
.newsletter{left:1033px;top:99px;width:52px;height:302px;background:var(--white)}
.newsletter span{position:absolute;left:14px;top:86px;writing-mode:vertical-rl;font-size:13.5px;letter-spacing:.8px;color:var(--pink)}
.side-heading{left:0;width:208px;height:32px;background:var(--orange-band);font-family:"Cinzel",serif;font-size:16.5px;padding:6px 0 0 27px;letter-spacing:.5px}
.side-list{left:27px;list-style:none;font-size:12px;line-height:25px}
.hero-left{left:216px;top:139px;width:448px;height:290px;background:linear-gradient(120deg,var(--teal-a),var(--teal-b));border:1px solid var(--white)}
.hero-person{left:528px;top:140px;width:112px;height:288px;background:linear-gradient(180deg,#c9a377 0%,#8f9a7d 35%,#e0394a 55%,#e6b79b 100%);opacity:.85}
.hero-script{left:240px;top:224px;width:282px;font-family:"Kalam",cursive;font-size:14.5px;line-height:18px;color:var(--ink)}
.search{left:240px;top:318px;width:208px;height:28px;background:var(--white);border:1px solid #c9c9c9;border-radius:3px;font-size:11px;color:#777;padding:6px 8px}
.search-btn{left:421px;top:322px;width:22px;height:20px;border:1px solid #bdbdbd;border-radius:2px;background:#f2f2f2}
.hero-right{left:677px;top:139px;width:343px;height:290px;background:#000;border:1px solid var(--white)}
.hero-right-text{left:712px;top:192px;width:290px;font-size:12px;line-height:15px}
.hero-baby{left:688px;top:268px;width:230px;height:140px;background:radial-gradient(ellipse at 55% 50%,#8a8a8a,#1a1a1a 70%,#000 100%)}
.ribbon{left:211px;top:451px;width:400px;height:40px}
.ribbon-label{left:265px;top:459px;font-family:"Cinzel",serif;font-size:16px;color:var(--ink);letter-spacing:.5px}
.artist-photo{left:231px;top:513px;width:77px;height:77px;background:linear-gradient(160deg,#f3e16a,#b78455 60%,#6b4a2e)}
.artist-text{left:317px;top:510px;width:335px;font-size:10.5px;line-height:14px}
.artist-text p+p{margin-top:13px}
.news-heading{left:681px;top:461px;font-family:"Cinzel",serif;font-size:15px;font-weight:400;letter-spacing:.6px}
.news-item{left:683px;width:320px;font-size:10.5px;line-height:14px;padding-left:19px}
.news-item::before{content:"";position:absolute;left:0;top:3px;width:8px;height:8px;background:var(--white);transform:rotate(45deg)}
.quote{left:224px;top:683px;width:782px;height:74px;background:var(--orange-quote)}
.quote-mark{left:247px;top:700px;width:34px;height:34px;border-radius:50%;background:#fcd27a}
.quote-text{left:300px;top:711px;width:690px;font-size:10.5px;line-height:14px;text-align:right}
.footer{top:789px;font-size:11px}
</style>
</head>
<body>
  <div class="abs pattern-side" role="img" aria-label="Decorative pattern of retro flowers in orange, green and black on brown"></div>
  <div class="abs pattern-bottom" role="img" aria-label="Decorative pattern of retro flowers in orange, green and black on brown"></div>

  <header class="abs header">
    <div class="abs studio-name">The Harlow Lane Studio</div>
    <a class="abs account-links" style="left:623px">your account</a>
    <a class="abs account-links" style="left:755px">view basket</a>
    <a class="abs account-links" style="left:879px">customer service</a>
    <nav>
      <span class="abs nav" style="left:211px">HOME</span>
      <span class="abs nav" style="left:310px">ARTIST GALLERY</span>
      <span class="abs nav" style="left:473px">SIGNATURES</span>
      <span class="abs nav" style="left:612px">BLOG</span>
      <span class="abs nav" style="left:707px">FRAMES</span>
      <span class="abs nav" style="left:815px">PRESS</span>
      <span class="abs nav" style="left:910px">CONTACT</span>
    </nav>
  </header>

  <div class="abs main"></div>
  <div class="abs newsletter"><span>SIGN UP FOR NEWSLETTER</span></div>

  <aside class="abs sidebar"></aside>
  <div class="abs side-heading" style="top:153px">ART STYLES</div>
  <ul class="abs side-list" style="top:183px">
    <li>Fine Art</li><li>Decorative Art</li><li>Vintage Art</li><li>Photography</li>
  </ul>
  <div class="abs side-heading" style="top:279px">SUBJECTS</div>
  <ul class="abs side-list" style="top:308px">
    <li>Abstract</li><li>Animals</li><li>Architecture</li><li>Art for Kids</li><li>Astronomy &amp; Space</li><li>Botanical</li><li>Fashion</li><li>Education</li><li>Fantasy</li><li>Figurative</li><li>Maps</li><li>Motivational</li><li>Music</li><li>Places</li><li>Scenic</li><li>Still Life</li><li>World Culture</li><li>more...</li>
  </ul>

  <section class="abs hero-left"></section>
  <div class="abs hero-person" role="img" aria-label="Photo of a smiling young woman in a patterned top and red skirt"></div>
  <p class="abs hero-script">Create custom books to celebrate birthdays and weddings, relive your travels, archive family recipes, or simply enjoy your everyday photos.</p>
  <div class="abs search">search here</div>
  <svg class="abs search-btn" viewBox="0 0 22 20"><circle cx="10" cy="9" r="4" fill="none" stroke="#555" stroke-width="1.5"/><line x1="13" y1="12" x2="16" y2="15" stroke="#555" stroke-width="1.8"/></svg>

  <section class="abs hero-right"></section>
  <p class="abs hero-right-text">Create custom books to celebrate birthdays and weddings, relive your travels, archive family recipes, or simply enjoy your everyday photos.</p>
  <div class="abs hero-baby" role="img" aria-label="Black and white photo of a baby lying on a dark background"></div>

  <svg class="abs ribbon" viewBox="0 0 400 40">
    <polygon points="0,6 40,6 40,36 0,36 14,21" fill="var(--ribbon)" stroke="var(--ribbon-edge)"/>
    <polygon points="400,6 360,6 360,36 400,36 386,21" fill="var(--ribbon)" stroke="var(--ribbon-edge)"/>
    <rect x="26" y="1" width="348" height="34" fill="#f4f6f9" stroke="var(--ribbon-edge)"/>
    <rect x="31" y="5" width="338" height="26" fill="none" stroke="var(--ribbon-edge)"/>
  </svg>
  <div class="abs ribbon-label">Artist Spotlight</div>
  <div class="abs artist-photo" role="img" aria-label="Portrait photo of the featured artist in a hat"></div>
  <div class="abs artist-text">
    <p>Create custom books to celebrate birthdays and weddings, relive your travels, archive family recipes, or simply enjoy your everyday photos. The easy-to-use book tool lets you customize every photo layout, background design, and caption. If you’re pressed for time, create an Express Photo Book in just minutes.</p>
    <p>Create custom books to celebrate birthdays and weddings, relive your travels, archive family recipes, or simply enjoy your everyday photos.</p>
  </div>

  <h2 class="abs news-heading">News and Blog</h2>
  <p class="abs news-item" style="top:498px">Create custom books to celebrate birthdays and weddings, relive your travels, archive family recipes, or simply enjoy your everyday photos.</p>
  <p class="abs news-item" style="top:561px">Create custom books to celebrate birthdays and weddings, relive your travels, archive family recipes, or simply enjoy your everyday photos.</p>

  <div class="abs quote"></div>
  <div class="abs quote-mark"></div>
  <p class="abs quote-text">" YAY! I'm so excited. I absolutely LOVE and have several Photo Books...Thanks again. Your product is the best, and so is your service."<br>- Dana R, photo book customer</p>

  <footer>
    <a class="abs footer" style="left:376px">FAQs</a>
    <a class="abs footer" style="left:428px">Privacy Policy</a>
    <a class="abs footer" style="left:524px">Terms of Use &amp; Legal</a>
    <a class="abs footer" style="left:664px">Store Policy</a>
    <a class="abs footer" style="left:761px">Site Map</a>
  </footer>
</body>
</html>
```